Flyer-Design für Schwimmtraining für Triathleten
Zielgruppe
Angebot
Schwimmen: als Personal Training, in Kleingruppen oder im Kraulkurs
Schwimmen: Videoanalysen
Triathlon: Trainingspläne, Leistungsdiagnostik
Zielgruppe des Flyers:
Triathleten jeder Leistungsklasse
Flyer ist a) als Auslage in Sportgeschäften, b) als Beilage in Wettkampftüten von Triathlonwettkämpfen gedacht
Aufgabenstellung
Triathleten sind tendenziell technisch orientierte Menschen, vergleichsweise wohlhabend. Schwimmen ist häufig eher die verhasste aber notwendige Teil der drei Disziplinen.
Bitte kein Standardformat für den Flyer.
Die Herausforderung bei einem Flyer als Beigabe zum Wettkampfbeutel: Überlicherweise wird der ganze Packen Werbung achtlos weggeworfen. Design und Format sollen dazu beitragen, dass der Flyer heraussticht und möglichst beachtet wird.
Grundsätzliche Infos: www.kelbrun42.de

```html
<!DOCTYPE html>
<html lang="de">
<head>
<meta charset="utf-8">
<title>Schwimmtraining für Triathleten – Flyer</title>
<link href="https://fonts.googleapis.com/css2?family=Archivo+Black&family=Libre+Franklin:wght@400;700;900&family=Oswald:wght@500;600&display=swap" rel="stylesheet">
<style>
  :root{
    --black:#0a0a0a;
    --white:#ffffff;
    --yellow:#f7e51c;
    --grey:#9a9a9a;
    --stage:#e9e9e7;
    --water-1:#5f8f90;
    --water-2:#3f6f73;
    --skin-1:#d9a98a;
    --skin-2:#b88565;
  }
  *{box-sizing:border-box;margin:0;padding:0}
  html,body{width:1200px;height:1200px;overflow:hidden;background:var(--stage)}
  body{position:relative;font-family:"Libre Franklin",Arial,sans-serif}

  .flyer{position:absolute;top:105px;width:452px;height:972px;overflow:hidden;background:var(--white)}
  .flyer--front{left:121px}
  .flyer--back{left:641px}
  .flyer__bg{position:absolute;inset:0}

  .headline{position:absolute;font-family:"Archivo Black",Arial,sans-serif;line-height:1;letter-spacing:0.5px}
  .front-headline{left:36px;top:40px;font-size:51px;color:var(--white)}
  .front-headline .accent{display:block;color:var(--yellow);margin-top:11px}
  .back-headline{left:36px;top:38px;font-size:46px;color:var(--black)}

  .offer{position:absolute;height:55px;padding-left:16px;display:flex;align-items:center;
    font-family:"Libre Franklin",Arial,sans-serif;font-weight:900;font-size:8.6px;line-height:1.3;color:var(--white);text-transform:uppercase}
  .offer::before{content:"";position:absolute;left:0;top:0;width:10px;height:100%;
    border:4px solid var(--white);border-right:none}
  .offer--athletik{left:257px;top:168px;align-items:flex-start;padding-top:9px}
  .offer--plaene{left:95px;top:195px;align-items:flex-start;padding-top:17px}
  .offer--schwimm{left:32px;top:267px;align-items:flex-start;padding-top:11px}
  .offer--video{left:287px;top:272px;align-items:flex-start;padding-top:15px}
  .offer--seminar{left:159px;top:342px}

  .badge{position:absolute;border-radius:50%;background:var(--yellow);display:flex;flex-direction:column;
    align-items:center;justify-content:center;text-align:center}
  .badge__inner{transform:rotate(-9deg);line-height:0.98}
  .badge__line{display:block;font-family:"Oswald",Arial,sans-serif;font-weight:600;color:var(--grey);letter-spacing:1px}
  .badge__line--strong{color:var(--black)}
  .badge__place{display:block;font-family:"Libre Franklin",Arial,sans-serif;font-weight:900;color:var(--black);line-height:1.15;margin-top:3px}
  .badge--front{left:-8px;top:363px;width:176px;height:176px}
  .badge--front .badge__line{font-size:24px}
  .badge--front .badge__line--strong{font-size:27px}
  .badge--front .badge__place{font-size:8px}
  .badge--back{left:265px;top:720px;width:190px;height:190px}
  .badge--back .badge__line{font-size:26px}
  .badge--back .badge__line--strong{font-size:29px}
  .badge--back .badge__place{font-size:8.6px}

  .photo{position:absolute}
  .photo--trainer{left:236px;top:386px;width:216px;height:586px;
    background:linear-gradient(180deg,#2b2b2b 0%,var(--skin-1) 18%,var(--skin-2) 60%,#1b1b1b 78%,var(--skin-1) 100%)}

  .quote{position:absolute;left:41px;top:556px;width:200px;font-size:10.6px;line-height:17.4px;color:var(--black);text-transform:uppercase}
  .quote strong{font-weight:900}
  .signature{position:absolute;left:92px;top:745px;width:140px;height:72px;background:#f1f1f1}

  .contact{position:absolute;font-size:9px;line-height:13px}
  .contact--front{left:41px;top:833px;width:140px;color:var(--black)}
  .contact--back{left:39px;top:840px;color:var(--white)}

  .brand{position:absolute;font-family:"Libre Franklin",Arial,sans-serif;font-weight:900;font-size:27px;letter-spacing:-0.5px}
  .brand--front{left:41px;top:895px;color:var(--black)}
  .brand--back{left:39px;top:890px;color:var(--white)}

  .back-lead{position:absolute;left:39px;top:404px;width:400px;font-family:"Libre Franklin",Arial,sans-serif;font-weight:900;font-size:15.5px;line-height:24px;color:var(--yellow);text-transform:uppercase}
  .back-body{position:absolute;left:39px;top:456px;width:380px;font-size:10.6px;line-height:18.5px;color:var(--white)}
  .back-body p+p{margin-top:6px}
  .back-body strong{font-weight:900}
  .back-cta{top:636px}

  .sender{position:absolute;left:39px;top:782px;font-size:9.2px;line-height:13px;color:var(--white)}
  .sender__name{display:block;font-weight:900;font-size:12.5px;line-height:16px}
  .pointer{position:absolute;left:163px;top:770px}

  .social{position:absolute;left:237px;top:922px;display:flex;align-items:center;gap:8px;
    font-weight:700;font-size:14px;color:var(--yellow)}
  .social__dot{width:22px;height:22px;border-radius:50%;background:var(--yellow)}
</style>
</head>
<body>

<section class="flyer flyer--front" aria-label="Flyer Vorderseite">
  <svg class="flyer__bg" width="452" height="972" viewBox="0 0 452 972" aria-hidden="true">
    <rect width="452" height="972" fill="var(--white)"/>
    <polygon points="0,0 452,0 452,419 0,514" fill="var(--black)"/>
  </svg>

  <h1 class="headline front-headline">MAKE WATER<span class="accent">YOUR FRIEND</span></h1>

  <div class="offer offer--athletik">Athletik- und<br>Stabilisierungstraining<br>als Personal Training</div>
  <div class="offer offer--plaene">Trainingspläne &amp;<br>Leistungsdiagnostik</div>
  <div class="offer offer--schwimm">Schwimmtraining –<br>als Personal Training in Klein-<br>gruppen oder im Kraulkurs</div>
  <div class="offer offer--video">Videoanalyse deiner<br>Schwimmtechnik</div>
  <div class="offer offer--seminar">Schwimmseminare</div>

  <div class="photo photo--trainer" role="img" aria-label="Foto: Schwimmtrainer mit Badekappe, Schwimmbrille und gelbem Pullbuoy"></div>

  <div class="badge badge--front">
    <div class="badge__inner">
      <span class="badge__line">SCHWIMM-</span>
      <span class="badge__line">TRAINING FÜR</span>
      <span class="badge__line badge__line--strong">TRIATHLETEN</span>
      <span class="badge__place">IN MÜNCHEN, MALLORCA<br>UND LIECHTENSTEIN</span>
    </div>
  </div>

  <p class="quote">„Servus und ein herzliches willkommen bei KELBRUN42, <strong>deinem Personal Trainer für Schwimmen, Triathlon und Ausdauersport</strong>. Ich biete dir Schwimmtechnik-Training, Kraulkurse, Trainingspläne &amp; Leistungsdiagnostik und Schwimmseminare an – in München, Mallorca und Liechtenstein.“</p>

  <div class="signature" role="img" aria-label="Handschriftliche Unterschrift: Malte"></div>

  <p class="contact contact--front">Melde dich mobil (0176-40318852) oder per E-Mail (malte@kelbrun42.de) bei mir!</p>

  <div class="brand brand--front">kelbrun42.de</div>
</section>

<section class="flyer flyer--back" aria-label="Flyer Rückseite">
  <svg class="flyer__bg" width="452" height="972" viewBox="0 0 452 972">
    <defs>
      <linearGradient id="water" x1="0" y1="0" x2="1" y2="1">
        <stop offset="0" stop-color="var(--water-1)"/>
        <stop offset="1" stop-color="var(--water-2)"/>
      </linearGradient>
      <linearGradient id="lake" x1="0" y1="0" x2="0" y2="1">
        <stop offset="0" stop-color="#8fb9c4"/>
        <stop offset="1" stop-color="#4d7d88"/>
      </linearGradient>
      <linearGradient id="green" x1="0" y1="0" x2="1" y2="0">
        <stop offset="0" stop-color="#c7cf6a"/>
        <stop offset="1" stop-color="#8fb88a"/>
      </linearGradient>
    </defs>
    <rect width="452" height="972" fill="var(--white)"/>
    <polygon points="0,387 452,311 452,972 0,972" fill="var(--black)"/>
    <polygon points="248,244 452,208 452,228 248,264" fill="var(--black)"/>
    <polygon points="0,160 234,122 234,336 0,375" fill="url(#water)" role="img" aria-label="Foto: Triathleten beim Kraulschwimmen im offenen Wasser"/>
    <polygon points="248,120 452,84 452,204 248,237" fill="url(#lake)" role="img" aria-label="Foto: Triathlet im Neoprenanzug steigt aus dem Wasser"/>
    <polygon points="248,264 452,228 452,297 248,329" fill="url(#green)" role="img" aria-label="Foto: Schwimmer neben gelber Wendeboje"/>
  </svg>

  <h2 class="headline back-headline">BEAT THE BEAST</h2>

  <p class="back-lead">Du suchst einen kompetenten Trainer<br>für Schwimmen oder Triathlon?</p>

  <div class="back-body">
    <p>Jemanden, der deine aktuellen Schwächen präzise analysiert, ein genau auf dich und deine Kompetenzen zugeschnittenes Personal Training entwirft und mit dir gemeinsam effizient und fokussiert an deinen Zielen arbeitet?</p>
    <p>Mein Name ist <strong>Malte Ostrander</strong> und dein Training bei mir profitiert nicht nur von vier Jahrzehnten persönlicher Wettkampferfahrung im Schwimm-, Triathlon- und Laufsport, sondern ebenso von meinen vielfältigen Ausbildungen zum Trainer, Ernährungsberater und systemischen Körpercoach.</p>
  </div>

  <p class="back-lead back-cta">Lass es uns gemeinsam angehen –<br>im Personal Training, in der<br>Kleingruppe oder in einem meiner<br>Kurse oder Seminare!</p>

  <p class="sender"><span class="sender__name">MALTE OSTRANDER</span>Fennerweg 14<br>81679 München</p>

  <svg class="pointer" width="74" height="30" viewBox="0 0 74 30" aria-hidden="true">
    <path d="M72 4 C50 8 28 14 6 22" fill="none" stroke="var(--yellow)" stroke-width="3.5" stroke-linecap="round"/>
    <path d="M16 10 L4 22 L20 27" fill="none" stroke="var(--yellow)" stroke-width="3.5" stroke-linecap="round" stroke-linejoin="round"/>
  </svg>

  <p class="contact contact--back">Melde dich mobil (0176-40318852) oder<br>per E-Mail (malte@kelbrun42.de) bei mir!</p>

  <div class="badge badge--back">
    <div class="badge__inner">
      <span class="badge__line">SCHWIMM-</span>
      <span class="badge__line">TRAINING FÜR</span>
      <span class="badge__line badge__line--strong">TRIATHLETEN</span>
      <span class="badge__place">IN MÜNCHEN, MALLORCA<br>UND LIECHTENSTEIN</span>
    </div>
  </div>

  <div class="brand brand--back">kelbrun42.de</div>

  <div class="social"><span class="social__dot"></span>@kelbrun42</div>
</section>

</body>
</html>
```